Business Performance Improvement Book Cover Design Project

We need a book cover design for a new company, based in Eastern Australia, called Varrow Global. We advise clients on process improvement, continuous improvement and business performance improvement, especially in the manufacturing areas and Fast Moving Consumer Goods industries.
We have a written a book designed to demonstrate our very high calibre of knowledge and to use as a marketing tool for prospective clients. We hope to give it out at training seminars and as a comprehensive business card.

Title of the book is: An integrated path to Operational Results Growth.
Subtitle: Shape a Steady Progress method to match your workplace values.
Author: by Martin Varrow
Back Cover: No need for a bar code in this edition. An important aspect is that we will distribute by hand. Text below for back page.

'For the experienced Business Performers, this book is designed to offer an insight into the advantages and an example of an approach to Business Improvement. It is not the only way but it is tried and tested in world class companies and it works. For those new to Continuous Improvement, it offers a helpful introduction to a holistic business improvement system, an overview of important success factors and pitfalls, recommendations on how to implement tools and methods and a quick guide to see when to use which tools. '

'Consultancies are one of many tools management teams can engage and management must make sure the consultants tailor their approach to suit its business needs and culture and not vice versa.'

End of text for back cover.

Business Performance Improvement is also known as or can include:
Continuous Improvement
Process Improvement
Lean Six Sigma
Operational Excellence
Total Productive Maintenance
Harlow Assembly Method
Total Quality Management
Business Process Re engineering
Output Levers
=
Varrow Global

The book size is 175 x 240 mm and will need a 10-15mm bleed. The spine is not known at this stage exactly and will need to be updated once the printing is finished but I suggest a 10mm until I have the exact size.

Our company colours are Pantone 288, R0,G75,B141, C100,M79,Y17,K3. Attached are some other publications that give a sense of what we like to portray, Some words which might add to this are: professional, elegance, quality, sleek.

Reason: After receiving the designs, I realised that I needed to update the brief with more and better quality information for designers to work with.

Target Market(s)

people in the accounting and insolvency industries, production managers and CEOs, Chief Operating Officers, members of the executive team of large companies and GMs of small companies.

Industry/Entity Type

Marketing

Requirements
Must have
• Communicate an image that shows an improvement or increase of something.
Very professional and elegant
Emphasis on the words 'Business Performance Improvement' in the title, subtitle also important
Must appeal to a high-end of the market audience
Nice to have
• Recommendation for your cover to be gloss or matt in print
Image can be indirectly related to money but not specifically
Somehow that it matches or is not so different to the attached brochure
Should not have
• Not be too loud or commercial
Book jacket. WIll be printed as soft cover first run and hard cover 2nd run

```html
<!DOCTYPE html>
<html lang="en">
<head>
<meta charset="utf-8">
<title>Varrow Global — Book Cover</title>
<link href="https://fonts.googleapis.com/css2?family=Baloo+2:wght@700&family=Exo+2:wght@300;400&display=swap" rel="stylesheet">
<style>
  :root {
    --page-bg: #e6e6e6;
    --cover-blue: #2a5a92;
    --photo-deep: #1c4f8f;
    --photo-mid: #2f78c0;
    --photo-light: #5aa2de;
    --suit-dark: #22262e;
    --growth-line: #7fd0ec;
    --text-white: #ffffff;
    --rule: rgba(255,255,255,0.8);
  }
  * { margin: 0; padding: 0; box-sizing: border-box; }
  html, body {
    width: 1200px; height: 900px; overflow: hidden;
    background: var(--page-bg);
  }
  .book-cover {
    position: absolute;
    left: 328px; top: 53px;
    width: 559px; height: 794px;
    background: var(--cover-blue);
    overflow: hidden;
    box-shadow: 0 2px 8px rgba(0,0,0,0.25);
  }
  .cover-photo {
    position: absolute; left: 0; top: 0;
    width: 100%; height: 464px;
    background:
      radial-gradient(ellipse 38% 62% at 50% 58%, var(--suit-dark) 0%, var(--suit-dark) 70%, transparent 100%),
      radial-gradient(ellipse at 82% 18%, var(--photo-light) 0%, transparent 55%),
      linear-gradient(160deg, var(--photo-mid) 0%, var(--photo-deep) 100%);
  }
  .growth-chart {
    position: absolute; left: 0; top: 0;
    width: 559px; height: 464px;
  }
  .cover-text {
    position: absolute; left: 43px; top: 502px; right: 24px;
    color: var(--text-white);
  }
  .author {
    display: inline-block;
    width: 358px;
    font-family: "Exo 2", sans-serif;
    font-weight: 300;
    font-size: 18px;
    padding-bottom: 5px;
    border-bottom: 2px solid var(--rule);
  }
  .title {
    margin-top: 14px;
    width: 480px;
    font-family: "Baloo 2", sans-serif;
    font-weight: 700;
    font-size: 28px;
    line-height: 36px;
  }
  .subtitle {
    margin-top: 12px;
    width: 230px;
    font-family: "Exo 2", sans-serif;
    font-weight: 300;
    font-size: 18px;
    line-height: 25px;
  }
  .publisher-mark {
    position: absolute; left: 336px; top: 712px;
    display: flex; align-items: center; gap: 10px;
    color: var(--text-white);
    font-family: "Exo 2", sans-serif;
    font-weight: 400;
    font-size: 26px;
  }
  .publisher-dot {
    width: 22px; height: 22px; border-radius: 50%;
    background: var(--text-white);
  }
</style>
</head>
<body>
  <main class="book-cover">
    <div class="cover-photo" role="img" aria-label="Photo of a businessman in a dark suit drawing a rising growth line on a blue world-map background"></div>
    <svg class="growth-chart" viewBox="0 0 559 464" aria-hidden="true">
      <polyline points="0,300 45,267 72,327 112,307 152,253 192,247 232,267 272,233 325,207 372,176"
        fill="none" stroke="var(--growth-line)" stroke-opacity="0.75" stroke-width="14"
        stroke-linejoin="round" stroke-linecap="round"/>
      <polygon points="350,168 405,140 385,196" fill="var(--growth-line)" fill-opacity="0.8"/>
    </svg>
    <section class="cover-text">
      <p class="author">Martin Varrow B. Mech Eng., M. Sc (NTA)</p>
      <h1 class="title">An integrated path to Operational Results Growth.</h1>
      <p class="subtitle">Shape a Steady Progress method to match your workplace values.</p>
    </section>
    <div class="publisher-mark">
      <span class="publisher-dot"></span>
      <span class="publisher-name">Varrow Global</span>
    </div>
  </main>
</body>
</html>
```